ivTorvan Employee-Centric Engagement brochure

Design a 2-page 81/2" x 11'' brochure (front and back) that includes our logo and some pictures. We need it in a format that we can print from and edit. Word or PDF would be good. We need to be able to give the file to a printing company or Brimlo office for them to print for us. We conduct frequent employee surveys as well as providing coaching to employees and managers around the data. Our goal is to get employees engaged in continuous improvement and in making their teams and workplace the best it can be. We have been in business for 20 years and this is an extension of what we have been doing in the past. Bringing the ownership of engagement and improvement to the employees rather than having managers responsible for employee engagement and process improvement. Our Energy metric is research based and predicts performance. Our web site is www.ivtorvan.com. I've attached a Word document with our first pass at content. Please improve greatly on this.

Target Market(s)

Company managers and senior HR personnel

Industry/Entity Type

Employee

Font styles to use
Sans Serif

Colors

Designer to choose colors to be used in the design.

Requirements
Must have
• All of the information in the documents sent and some appropriate pictures/background

```html
<!DOCTYPE html>
<html lang="en">
<head>
<meta charset="utf-8">
<title>ivTorvan Employee-Centric Engagement Brochure</title>
<link href="https://fonts.googleapis.com/css2?family=Ubuntu:ital,wght@0,300;0,400;0,500;0,700;1,400&display=swap" rel="stylesheet">
<style>
  :root{
    --backdrop:#6d6d6d;
    --paper:#ffffff;
    --ink:#1d1d1d;
    --body:#555555;
    --sky:#3db8e8;
    --sky-soft:#c9e7f7;
    --orange:#f07a24;
    --bubble:#e2e2e2;
    --bubble-text:#333333;
    --photo-dark:#1a1a1a;
    --photo-wood:#9a5b33;
  }
  *{margin:0;padding:0;box-sizing:border-box}
  html,body{width:1200px;height:1200px;overflow:hidden;background:var(--backdrop);font-family:"Ubuntu",sans-serif}
  .stage{position:absolute;left:0;top:0;width:1237px;height:1237px;transform:scale(0.9701);transform-origin:0 0}
  .page{position:absolute;top:274px;width:559px;height:723px;background:var(--paper);overflow:hidden;box-shadow:0 0 18px rgba(0,0,0,.35)}
  .page--front{left:44px;
    background:
      linear-gradient(to bottom,rgba(255,255,255,0) 62%,#fff 96%),
      linear-gradient(90deg,#c2e4f6 0,#e1f1fb 49%,#fff 49.2%);}
  .page--back{left:628px}
  .abs{position:absolute}
  .hero{left:0;top:0}
  .headline{left:0;width:562px;top:224px;text-align:center;font-size:24.5px;font-weight:500;letter-spacing:1.3px;line-height:28.5px;color:var(--ink)}
  .col-title{font-size:18px;font-weight:700;color:var(--sky);letter-spacing:.2px}
  .col-left{left:60px;top:305px;width:210px}
  .col-right{left:297px;top:305px;width:240px}
  .bullets{list-style:none;margin-top:12px;font-size:11px;font-weight:300;color:var(--body);line-height:15px}
  .bullets li{margin-bottom:4.5px;padding-left:8px;text-indent:-8px}
  .bullets li::before{content:"•";display:inline-block;width:8px;text-indent:0}
  .roles{left:0;width:562px;top:520px;text-align:center;font-size:12px;font-weight:700;letter-spacing:3px;line-height:15.5px;color:var(--ink)}
  .quote{left:0;width:562px;top:554px;text-align:center;font-size:12px;font-weight:500;color:var(--orange)}
  .summary{left:44px;width:478px;top:576px;text-align:center;font-size:10px;font-weight:300;line-height:13.3px;color:#333}
  .roles-note{left:0;width:562px;top:658px;text-align:center;font-size:8px;font-style:italic;line-height:11px;color:#333}
  .back-title{left:0;width:562px;top:24px;text-align:center;font-size:29px;font-weight:500;letter-spacing:1px;line-height:34px;color:var(--ink)}
  .cycle{left:0;top:0}
  .cycle text{font-family:"Ubuntu",sans-serif;font-size:11px;fill:var(--bubble-text);text-anchor:middle}
  .cycle text.wheel-name{font-size:19px;font-weight:500;fill:var(--orange);text-anchor:start}
  .tagline{left:0;width:559px;top:593px;text-align:center;font-size:14px;font-weight:500;line-height:17px;color:var(--orange)}
  .contact-band{left:0;top:636px;width:559px;height:87px;background:var(--sky);color:#fff;text-align:center;padding-top:12px}
  .contact-band .call{font-size:18px;font-weight:300}
  .contact-band .call b{font-weight:500}
  .contact-band .mail{font-size:14px;font-weight:300;margin-top:1px}
  .contact-band .web{font-size:15.5px;font-weight:500;margin-top:2px}
</style>
</head>
<body>
<div class="stage">

  <section class="page page--front">
    <svg class="abs hero" width="559" height="300" viewBox="0 0 559 300">
      <defs>
        <clipPath id="heroDisc"><circle cx="281" cy="166" r="215"/></clipPath>
        <linearGradient id="heroPhotoTone" x1="0" y1="0" x2="0" y2="1">
          <stop offset="0" stop-color="var(--photo-dark)"/>
          <stop offset=".7" stop-color="#2a211c"/>
          <stop offset="1" stop-color="var(--photo-wood)"/>
        </linearGradient>
      </defs>
      <circle cx="281" cy="166" r="215" fill="#ffffff"/>
      <g clip-path="url(#heroDisc)">
        <rect x="60" y="-60" width="450" height="258" fill="url(#heroPhotoTone)" role="img" aria-label="Photo: a hand placing a target block on top of stacked wooden steps marked with a person, ideas and gears"/>
      </g>
      <circle cx="193" cy="37" r="25" fill="var(--sky)"/>
      <text x="222" y="47" font-family="Ubuntu, sans-serif" font-size="30" font-weight="500" fill="var(--orange)">ivTorvan</text>
    </svg>

    <h1 class="abs headline">FOCUS EMPLOYEE ENERGY<br>ON WHAT REALLY MATTERS</h1>

    <div class="abs col-left">
      <h2 class="col-title">BY MOVING UP TO</h2>
      <ul class="bullets">
        <li>Empowering employees to own their own engagement and energy</li>
        <li>Managers are teachers and advisors vs. survey interpreters</li>
        <li>On-going and frequent process built the way you do business</li>
        <li>Backed by the science of human energy at work</li>
        <li>Documented return on investment (ROI)</li>
      </ul>
    </div>

    <div class="abs col-right">
      <h2 class="col-title">SIMPLE * FAST * PROVEN</h2>
      <ul class="bullets">
        <li>Transforming employee engagement with a proven model</li>
        <li>Simple and fast implementation</li>
        <li>Quick and easy process for users</li>
        <li>Celebrations focused on documented results</li>
      </ul>
    </div>

    <svg class="abs" style="left:268px;top:448px" width="291" height="46" viewBox="0 0 291 46">
      <circle cx="7" cy="22" r="6" fill="#ffffff"/>
      <polyline fill="none" stroke="#9fd6f1" stroke-width="1.4"
        points="13,22 38,22 44,14 50,28 56,8 62,30 68,18 74,22 140,22 146,6 152,36 158,14 164,26 170,22 236,22 242,30 248,10 254,34 260,4 266,26 272,22 278,8 284,30 291,18"/>
    </svg>

    <p class="abs roles">CHANGING THE ROLES OF ENGAGEMENT<br>CHANGING THE ATTITUDES OF ENGAGEMENT</p>
    <p class="abs quote">“IT WORKS; NOT A SURVEY; LEARNING FOR ALL”</p>
    <p class="abs summary">Employee-centric engagement uses a new lens to bring people together to drive positive change. Through a data-driven process, frequent pulsing is focused on the employee learning from their own data. Employees learn and reflect and then engage with peer ambassadors who use root-cause analysis, ideation and other tools to focus learning and present 3 improvement ideas to managers. Return on investment projections are done for each idea.</p>
    <p class="abs roles-note">Managers delegate, coach and teach.<br>Ambassadors are facilitators and co-creators.<br>Employees are agents of change and improvement.</p>
  </section>

  <section class="page page--back">
    <h1 class="abs back-title">EMPLOYEE-CENTRIC<br>ENGAGEMENT PROCESS</h1>

    <svg class="abs cycle" width="559" height="600" viewBox="0 0 559 600">
      <defs>
        <linearGradient id="wheelTone" x1="0" y1="0" x2="1" y2="1">
          <stop offset="0" stop-color="#39b54a"/>
          <stop offset=".35" stop-color="#f2e51a"/>
          <stop offset=".6" stop-color="#e9232e"/>
          <stop offset=".8" stop-color="#8e3a9c"/>
          <stop offset="1" stop-color="#3f4fae"/>
        </linearGradient>
      </defs>
      <g fill="var(--bubble)">
        <circle cx="165" cy="216" r="68"/>
        <circle cx="384" cy="211" r="68"/>
        <circle cx="467" cy="416" r="70"/>
        <circle cx="296" cy="521" r="68"/>
        <circle cx="122" cy="428" r="68"/>
      </g>
      <g fill="#bcbcbc">
        <circle cx="251" cy="192" r="6"/>
        <circle cx="272" cy="152" r="7"/>
        <circle cx="291" cy="192" r="9"/>
        <circle cx="86" cy="265" r="7"/>
        <circle cx="142" cy="333" r="9"/>
        <circle cx="441" cy="311" r="9"/>
        <circle cx="491" cy="280" r="11"/>
        <circle cx="210" cy="469" r="8"/>
      </g>
      <circle cx="287" cy="349" r="92" fill="none" stroke-width="72" stroke="url(#wheelTone)"/>
      <circle cx="287" cy="349" r="56" fill="#ffffff"/>
      <circle cx="247" cy="350" r="13" fill="var(--sky)"/>
      <text class="wheel-name" x="264" y="356">ivTorvan</text>

      <g fill="var(--sky)">
        <circle cx="224" cy="158" r="24"/>
        <circle cx="452" cy="245" r="24"/>
        <circle cx="407" cy="486" r="24"/>
        <circle cx="211" cy="514" r="24"/>
        <circle cx="97" cy="314" r="24"/>
      </g>
      <g fill="#ffffff">
        <path d="M-11,-4 h10 v-7 l12,11 -12,11 v-7 h-10z" transform="translate(224 158) rotate(-15)"/>
        <path d="M-11,-4 h10 v-7 l12,11 -12,11 v-7 h-10z" transform="translate(452 245) rotate(50)"/>
        <path d="M-11,-4 h10 v-7 l12,11 -12,11 v-7 h-10z" transform="translate(407 486) rotate(135)"/>
        <path d="M-11,-4 h10 v-7 l12,11 -12,11 v-7 h-10z" transform="translate(211 514) rotate(195)"/>
        <path d="M-11,-4 h10 v-7 l12,11 -12,11 v-7 h-10z" transform="translate(97 314) rotate(-90)"/>
      </g>

      <text x="165" y="206">MANAGER HELPS</text>
      <text x="165" y="219">FACILITATE</text>
      <text x="165" y="232">IMPLEMENTATION</text>
      <text x="384" y="196">FREQUENT PULSING</text>
      <text x="384" y="209">(3 TO 5 QUESTIONS TO</text>
      <text x="384" y="222">SPARK LEARNING)</text>
      <text x="462" y="417">EMPLOYEES REVIEW</text>
      <text x="462" y="430">TREND DATA AND</text>
      <text x="462" y="443">JOURNAL</text>
      <text x="296" y="514">AMBASSADORS</text>
      <text x="296" y="527">GUIDE IMPROVEMENT</text>
      <text x="296" y="540">DIALOGUE</text>
      <text x="120" y="428">3 IDEAS PRESENTED</text>
      <text x="120" y="441">TO MANAGER</text>
    </svg>

    <p class="abs tagline">ENHANCE FIRM PERFORMANCE BY CHANGING HOW YOUR<br>BUSINESS LISTENS AND LEARNS.</p>

    <footer class="abs contact-band">
      <p class="call">Call today: <b>+1 555-014-2290</b></p>
      <p class="mail">e-mail: info@ivtorvan.com</p>
      <p class="web">www.ivtorvan.com</p>
    </footer>
  </section>

</div>
</body>
</html>
```